corporate design for "Welsenhütte" a lodge hotel in one of the most famous parts in Germany.

What we need is a design for our Lodge. We offer 136 Beds in 29 Rooms on the mountain in famous Garmisch-Partenkirchen. Our guests have a straight sight to the top of Zugspitze which is the highest peak of germany. We have some very different business models. 1. Most of the year we host birthday party groups and wedding groups. Usually they come for two days to have great celebrations here with about 60-120 gueste "exclusive". 2. Especially befoe x-mas but also durig the year we have companies here, to hold strategy meetings, or teambuilding events (we want to grow that business especially). 3. during the week we host school classes to get the "hotel" fully booked.
What we need is a coorparate style including logo, website, cards, etc. the whole programm.
The main focus is "wood, mauntains, wilderness, lodge,..."
I will upload some pictures and the logo so far.
What I really like is a theme called KALDWEN (www.kldtheme-demo.com) with all its parallax and background style. Our website so far is www.welsenhuette-demo.com.
Budget is not the issue as long as it is really looking amazing.

Industry/Entity Type
Hotel
Logo Text
Welsenhütte Garmisch-Partenkirchen
Number of Pages Required
1 page
Requirements
Must have
- I want to host the page in WIX. It has to be responsive and very modern.

```html
<!DOCTYPE html>
<html lang="en">
<head>
<meta charset="utf-8">
<title>Welsenhütte – Garmisch-Partenkirchen</title>
<link href="https://fonts.googleapis.com/css2?family=Kaushan+Script&family=Open+Sans:ital,wght@0,400;0,600;0,700;1,400&family=Oswald:wght@400;500&display=swap" rel="stylesheet">
<style>
:root{
  --tan:#bf986a;
  --tan-dark:#a98253;
  --ink:#2a2a2a;
  --text:#555;
  --paper:#efefef;
  --white:#fff;
  --night:#1f2226;
  --footer:#2b2b2b;
}
*{box-sizing:border-box;margin:0;padding:0}
html,body{width:1200px;height:3403px;overflow:hidden}
body{font-family:"Open Sans",sans-serif;color:var(--text);background:var(--paper);position:relative}
.accent{color:var(--tan)}
.btn{display:inline-block;background:var(--tan);color:var(--white);font-family:"Oswald",sans-serif;text-transform:uppercase;letter-spacing:.5px;font-size:15px;padding:8px 18px}
.btn-light{background:var(--white);color:var(--tan-dark)}
.photo{position:absolute}

/* hero */
.hero{position:absolute;top:0;left:0;width:1200px;height:560px;
  background:linear-gradient(180deg,#4f5a48 0%,#6f7a5a 30%,#8a7b5e 60%,#5a4b37 100%)}
.hero::after{content:"";position:absolute;inset:0;background:rgba(20,20,15,.25)}
.brand{position:absolute;left:165px;top:14px;z-index:2;color:var(--white)}
.brand-name{font-family:"Oswald",sans-serif;font-size:34px;font-weight:500;line-height:1}
.brand-sub{font-family:"Oswald",sans-serif;font-size:15px;font-weight:500;margin-top:4px}
.brand-dot{display:inline-block;width:34px;height:34px;border-radius:50%;background:var(--white);vertical-align:middle;margin-right:10px}
.contact-top{position:absolute;top:34px;right:165px;z-index:2;color:var(--white);font-size:15px;display:flex;gap:24px;align-items:center}
.contact-top span{display:flex;gap:7px;align-items:center}
.nav{position:absolute;left:159px;top:95px;width:878px;height:38px;background:var(--tan);z-index:2;display:flex;align-items:center}
.nav a{color:var(--white);font-family:"Oswald",sans-serif;text-transform:uppercase;font-size:15px;text-decoration:none;padding:0 27px;height:38px;line-height:38px;white-space:nowrap}
.nav a.active{background:var(--paper);color:var(--ink)}
.hero-copy{position:absolute;top:262px;left:0;width:1200px;text-align:center;color:var(--white);z-index:2}
.hero-copy h1{font-family:"Kaushan Script",cursive;font-size:44px;font-weight:400;text-shadow:0 2px 4px rgba(0,0,0,.4)}
.hero-copy p{font-size:18px;margin-top:6px}
.hero-copy .btn{margin-top:44px;font-size:17px;padding:8px 20px}
.arrow-thin{position:absolute;top:280px;z-index:2;color:rgba(255,255,255,.8);font-size:40px}

/* section titles */
.sec-title{position:absolute;left:0;width:1200px;text-align:center;font-family:"Kaushan Script",cursive;font-size:46px;font-weight:400;color:var(--ink)}
.sec-mark{position:absolute;left:585px;width:30px;height:30px;border-radius:50%;background:var(--ink)}

/* welcome */
.welcome{position:absolute;top:560px;left:0;width:1200px;height:381px;background:var(--paper)}
.welcome p{position:absolute;top:200px;left:190px;width:820px;text-align:center;font-size:12.5px;line-height:22px;color:var(--text)}
.welcome .btn{position:absolute;top:284px;left:536px}

/* split */
.split{position:absolute;left:0;width:1200px;height:318px}
.panel{position:absolute;top:0;width:600px;height:318px;background:var(--tan);color:var(--white);padding:28px 40px 0 162px}
.panel h3{font-family:"Oswald",sans-serif;font-weight:500;font-size:16px;text-transform:uppercase;margin-bottom:10px;line-height:22px}
.panel p{font-size:12px;line-height:19px}
.panel ul{list-style:none}
.panel li{font-size:11.5px;line-height:17px;display:flex;gap:8px;margin-bottom:9px}
.panel li svg{flex:none;margin-top:2px}
.panel .btn{margin-top:14px;font-size:13px;padding:6px 12px}

/* services & activities */
.services{position:absolute;top:1576px;left:0;width:1200px;height:506px;background:var(--paper)}
.activities{position:absolute;top:2082px;left:0;width:1200px;height:560px;
  background:linear-gradient(180deg,#3a3f44 0%,#262a2e 45%,#1a1c1e 100%)}
.cards{position:absolute;top:182px;left:160px;width:880px;display:flex;justify-content:space-between}
.activities .cards{top:202px}
.card{width:266px;text-align:center}
.card .img{height:170px}
.activities .card .img{height:188px}
.card h4{font-family:"Oswald",sans-serif;font-weight:500;font-size:16px;color:var(--ink);margin-top:20px;text-transform:uppercase}
.card p{font-size:12px;line-height:18px;margin-top:6px;padding:0 18px}
.activities .card h4,.activities .card p{color:var(--white)}
.circle-arrow{position:absolute;width:34px;height:34px;border-radius:50%;background:var(--white);border:1px solid #ccc;display:flex;align-items:center;justify-content:center}

/* testimonials */
.testimonials{position:absolute;top:2642px;left:0;width:1200px;height:540px;background:var(--paper)}
.avatars{position:absolute;top:192px;left:270px;width:660px;display:flex;justify-content:space-between}
.person{width:120px;text-align:center}
.avatar{width:90px;height:90px;border-radius:50%;margin:0 auto;border:3px solid var(--tan);background:linear-gradient(160deg,#d9b79a,#8d6a55)}
.person span{display:block;font-size:12px;margin-top:12px;color:var(--text)}
.person.active span{color:var(--tan)}
.quote{position:absolute;top:352px;left:159px;width:880px;height:113px;background:var(--white);box-shadow:0 1px 4px rgba(0,0,0,.12);padding:22px 40px;text-align:center;font-style:italic;font-size:13px;line-height:21px;color:#777}
.quote b{font-family:Georgia,serif;font-size:30px;color:#ccc;font-style:normal;line-height:0}

/* footer */
.footer{position:absolute;top:3140px;left:0;width:1200px;height:263px}
.footer-body{position:absolute;top:35px;left:0;width:1200px;height:193px;background:var(--footer)}
.fcol{position:absolute;top:38px;color:#ccc;font-size:11.5px;line-height:19px}
.fcol h5{font-family:"Kaushan Script",cursive;font-weight:400;font-size:17px;color:var(--white);margin-bottom:6px;padding-bottom:2px;border-bottom:1px solid #555;width:160px}
.fcol li{list-style:none}
.fcol li::before{content:"› ";color:var(--tan)}
.fcol input{display:block;width:160px;height:24px;border:0;margin:8px 0 10px;padding:0 6px;font-size:11px;font-family:"Open Sans",sans-serif}
.fcol .btn{font-size:13px;padding:5px 10px}
.footer-brand{position:absolute;top:62px;left:772px;color:var(--white)}
.copyright{position:absolute;top:228px;left:0;width:1200px;height:35px;background:var(--tan);color:var(--white);text-align:center;font-size:12px;line-height:35px}
</style>
</head>
<body>

<header class="hero">
  <div class="photo" role="img" aria-label="Wooden mountain lodge terrace with forest and mountains" style="inset:0"></div>
  <div class="brand">
    <div class="brand-name"><span class="brand-dot"></span>Welsenhütte</div>
    <div class="brand-sub" style="padding-left:44px">Garmisch-Partenkirchen</div>
  </div>
  <div class="contact-top">
    <span><svg width="16" height="16" viewBox="0 0 24 24"><circle cx="12" cy="12" r="12" fill="#fff"/><path d="M8 6l2 3-1 1c1 2 2 3 4 4l1-1 3 2-1 2c-5 0-10-5-10-10z" fill="#333"/></svg>+49 (0)8800 / 4120</span>
    <span><svg width="16" height="12" viewBox="0 0 16 12"><rect width="16" height="12" fill="#fff"/><path d="M0 0l8 6 8-6" stroke="#333" fill="none"/></svg>info@welsenhuette-demo.com</span>
  </div>
  <nav class="nav">
    <a class="active">Home</a><a>The Welsen Hut</a><a>For Groups</a><a>For Companies</a><a>To Celebrate</a><a>With Many Activities</a>
  </nav>
  <div class="arrow-thin" style="left:88px">‹</div>
  <div class="arrow-thin" style="right:88px">›</div>
  <div class="hero-copy">
    <h1>Celebrate Your Events &amp; Moments With Us...</h1>
    <p>With Us It Can Be In Rustic Mountain Lodge Atmosphere Pleasant And Cozy Celebrations</p>
    <span class="btn">Call Us Now</span>
  </div>
</header>

<section class="welcome">
  <div class="sec-mark" style="top:62px"></div>
  <h2 class="sec-title" style="top:120px">Welcome To <span class="accent">Welsenhütte</span></h2>
  <p>Welcome on our sites! Above Garmisch-Partenkirchen, located right on the mountain, there is the Lärchenkopf- &amp; Welsenhütte. With 122 beds, the ideal group &amp; Event hut in Zugspitzland! The Lärchenkopf- &amp; Welsenhütte situated on a picturesque clearing in the middle on the mountain above Garmisch-Partenkirchen. Beneath the imposing Alpine peaks</p>
  <span class="btn">Read More</span>
</section>

<section class="split" style="top:941px">
  <div class="panel" style="left:0">
    <h3>The Welsen Hut Offers</h3>
    <p>The Welsen hut offers 136 beds in three houses. The rooms are divided into two categories. Firstly, there are rooms with bathroom (shower / WC), the other rooms with shared bathrooms / WC. The higher category with bath costs 40,- Euro per adult and night. The lower category with shared bathroom 30 Euro per adult and night. Children are of course cheaper, depending on age. Depending on the number of guests and the occasion of the event we forgive all our premises exclusively. This limit is a wedding with about 70 guests, which would be the case for you. That you can download our room plan down and your guests</p>
    <span class="btn btn-light">Read More</span>
  </div>
  <div class="photo" role="img" aria-label="Wooden lodge buildings among fir trees" style="left:600px;top:0;width:600px;height:318px;background:linear-gradient(160deg,#8fa6b8 0%,#5c6b4a 40%,#7a5a3e 100%)"></div>
</section>

<section class="split" style="top:1259px">
  <div class="photo" role="img" aria-label="Guests at tables on a sunny terrace in the mountains" style="left:0;top:0;width:600px;height:318px;background:linear-gradient(160deg,#6f8fa8 0%,#5a7a45 45%,#8a6b4b 100%)"></div>
  <div class="panel" style="left:600px;padding:28px 160px 0 14px">
    <h3>The Hosts Then Take Over Most Of The Costs At The Actual Day Of Celebration.</h3>
    <ul>
      <li><svg width="12" height="12" viewBox="0 0 12 12"><path d="M1 6l3 3 7-7" stroke="#fff" stroke-width="2" fill="none"/></svg>From 8:00 am to approximately 11:00 am breakfast for the guests who have already arrived Friday. Breakfast is included in the room rate.</li>
      <li><svg width="12" height="12" viewBox="0 0 12 12"><path d="M1 6l3 3 7-7" stroke="#fff" stroke-width="2" fill="none"/></svg>The event "Brotzeit" (from here you host) with snack plates, bread basket, pretzels, freshly baked meatloaf with potato salad, etc. at the self-service buffet with beverage service.</li>
      <li><svg width="12" height="12" viewBox="0 0 12 12"><path d="M1 6l3 3 7-7" stroke="#fff" stroke-width="2" fill="none"/></svg>Hier wird zum Auftakt oftmals ein Fass Bier vom Gastgeber bzw. Brautpaar angezapft, und / oder ein anderes „Welcome-Getränk" (Prosecco, Hugo, Spritz) ausgeschenkt.</li>
    </ul>
    <span class="btn btn-light" style="margin-top:4px">Read More</span>
  </div>
</section>

<section class="services">
  <div class="sec-mark" style="top:50px"></div>
  <h2 class="sec-title" style="top:108px">Our <span class="accent">Services</span></h2>
  <div class="circle-arrow" style="left:92px;top:248px"><svg width="10" height="12" viewBox="0 0 10 12"><path d="M8 1L2 6l6 5" stroke="#333" stroke-width="2" fill="none"/></svg></div>
  <div class="circle-arrow" style="left:1072px;top:248px"><svg width="10" height="12" viewBox="0 0 10 12"><path d="M2 1l6 5-6 5" stroke="#333" stroke-width="2" fill="none"/></svg></div>
  <div class="cards">
    <div class="card"><div class="img" role="img" aria-label="Festive dining room with laid tables" style="background:linear-gradient(160deg,#c98a5e,#8a3e2a)"></div><h4>Pictures / Impressions</h4><p>A collection of images that our cabin resort, and the surrounding countryside and impressions shows...[+]</p></div>
    <div class="card"><div class="img" role="img" aria-label="Coach bus for guest pick-up" style="background:linear-gradient(180deg,#e8ecef,#a7b14e 55%,#4a4a3a)"></div><h4>Arrival / Pick-Up Service</h4><p>No matter what kind of a celebration, a quaint Bavarian Berghütt'n always creates a special atmosphere...[+]</p></div>
    <div class="card"><div class="img" role="img" aria-label="Alpine valley with snowy peaks" style="background:linear-gradient(180deg,#6d9cc9,#d9e2ea 40%,#5e7d43 75%,#3f5a2e)"></div><h4>Map / Area</h4><p>An interactive map shows Tour suggestions, destinations and free activities around our Hütt'n. Explore...[+]</p></div>
  </div>
</section>

<section class="activities" role="img" aria-label="Dark mountain panorama at dusk">
  <div class="sec-mark" style="top:52px;background:var(--white)"></div>
  <h2 class="sec-title" style="top:118px;color:var(--white)">With Many Activities</h2>
  <div class="circle-arrow" style="left:92px;top:280px"><svg width="10" height="12" viewBox="0 0 10 12"><path d="M8 1L2 6l6 5" stroke="#333" stroke-width="2" fill="none"/></svg></div>
  <div class="circle-arrow" style="left:1072px;top:280px"><svg width="10" height="12" viewBox="0 0 10 12"><path d="M2 1l6 5-6 5" stroke="#333" stroke-width="2" fill="none"/></svg></div>
  <div class="cards">
    <div class="card"><div class="img" role="img" aria-label="School group outdoors on a meadow" style="background:linear-gradient(160deg,#9ab0c4,#6f8a4e 50%,#7a5a4a)"></div><h4>School Trip &amp; Group Tours</h4><p>The Lärchenkopf- and Welsenhütte is ideal suitable for school trips, youth groups, club outings...[+]</p></div>
    <div class="card"><div class="img" role="img" aria-label="Traditional festival parade in a village street" style="background:linear-gradient(160deg,#8aa0b2,#3a5a36 50%,#6a4a3a)"></div><h4>Festivals &amp; Celebrations</h4><p>No matter what kind of a celebration, a quaint Bavarian Berghütt'n always creates a special atmosphere...[+]</p></div>
    <div class="card"><div class="img" role="img" aria-label="Hikers resting on an alpine meadow" style="background:linear-gradient(180deg,#7aa3cc,#c8d2d8 35%,#6f9a4a 65%,#4e7a35)"></div><h4>Outdoor &amp; Adventure</h4><p>The following activities, tours and excursions with us and in the immediate vicinity...[+]</p></div>
  </div>
</section>

<section class="testimonials">
  <div class="sec-mark" style="top:52px"></div>
  <h2 class="sec-title" style="top:118px">Clients <span class="accent">Testimonials</span></h2>
  <div style="position:absolute;left:236px;top:222px;font-size:30px;color:#bbb">‹</div>
  <div style="position:absolute;left:950px;top:222px;font-size:30px;color:#bbb">›</div>
  <div class="avatars">
    <div class="person active"><div class="avatar" role="img" aria-label="Guest portrait"></div><span>Mr. Jonas Berger</span></div>
    <div class="person"><div class="avatar" role="img" aria-label="Guest portrait"></div><span>Mrs. Lena Hofer</span></div>
    <div class="person"><div class="avatar" role="img" aria-label="Guest portrait"></div><span>Mr. Paul Maier</span></div>
    <div class="person"><div class="avatar" role="img" aria-label="Guest portrait"></div><span>Miss Anna Kogler</span></div>
  </div>
  <div class="quote"><b>“</b> Lorem ipsum dolor sitamet, consectetuer adipiscing sed diam nonummy nibh euismod tincidunt ut laoreet dolore magna aliqua volutpat. Ut wisi enim ad minim veniam, quis nostrud exerci tation ullamcorper suscipit lobortis nisl ut aliquip ex ea commodo consequat. Duis autem vel eum iriure dolor in hendrerit in vulputate velit esse molestie consequat. <b>”</b></div>
</section>

<footer class="footer">
  <svg width="1200" height="60" viewBox="0 0 1200 60" style="position:absolute;top:0;left:0">
    <path d="M0 30 C300 -5 700 -5 1200 22 L1200 60 L0 60Z" fill="var(--tan)"/>
    <path d="M0 44 C300 10 700 12 1200 38 L1200 60 L0 60Z" fill="var(--footer)"/>
  </svg>
  <div class="footer-body">
    <div class="fcol" style="left:163px"><h5>Quick Links</h5>
      <ul><li>Home</li><li>The Welsen Hut</li><li>For Groups</li><li>For Companies</li><li>To Celebrate</li><li>With Many Activities</li></ul></div>
    <div class="fcol" style="left:345px"><h5>Contact Detail</h5>
      <div style="color:#fff;font-weight:600">WELSENHÜTTE<br>Almweg 12, 82467<br>Garmisch-Partenkirchen</div>
      <div style="margin-top:6px">☏ +49 (0)8800 / 4120</div>
      <div>☏ +49 (0)8800 / 4121</div>
      <div>✉ info@welsenhuette-demo.com</div></div>
    <div class="fcol" style="left:553px"><h5>Newsletter Signup</h5>
      <div>Get latest updates by entering your<br>email address</div>
      <input type="text" placeholder="Email Address">
      <span class="btn">Subscribe</span></div>
    <div class="footer-brand">
      <div class="brand-name"><span class="brand-dot"></span>Welsenhütte</div>
      <div class="brand-sub" style="padding-left:44px">Garmisch-Partenkirchen</div>
    </div>
  </div>
  <div class="copyright">© 2016 Welsenhütte, LLC All Rights Reserved</div>
</footer>

</body>
</html>
```